Gravelcraft Lip Balm. It is formulated with men in mind but other people certainly can use it.

The over arching name of the project is Tusker - which needs to be in the label somewhere, but Gravelcraft is the title.
It would be for a round jar container.
It is out of promoting products for men to open discussion about health issues that men often not talk about. As each product is created it will have a message to men about the health issue and where to find information, seek help or just be able to talk about it.
I would like darker colours (black) as the base but using other colours to
for the wording and design.
I am open to ideas on the layout, I have included some ideas, and also some of my own labelling ideas that I have worked on. I do like the carbon fibre background look that I have for my tusker label. I have also included my allgood label with some colour ideas.
I also was wondering about making it a after tattoo balm so that it can also be used as a lip balm as well…two for the price of one..basically the same ingredients are used.
They may change the look of the intended artwork..but I leave it in your skill full hands.
My number is +61490218537. You can txt me if you need some clarification.
Thank you
Kind regards and blessings

Target Market(s)

Target market is men of all ages as they can all be affected by one health issue or another at different times of life

Industry/Entity Type

Healthcare and beauty

Font styles to use
Sans Serif
Decorative

Requirements
Must have
• I still need to indeed to ingredients and container size.
Nice to have
• A novel and different look from the usual crowd that try to hard to look cool or funky

```html
<!DOCTYPE html>
<html lang="en">
<head>
<meta charset="utf-8">
<title>Gravelcraft Lip &amp; Tattoo Balm – Lid Label</title>
<link rel="stylesheet" href="https://fonts.googleapis.com/css2?family=Bebas+Neue&family=Oswald:wght@400;500&display=swap">
<style>
  :root {
    --backdrop: #e4e4e4;
    --lid-rim: #0c0c0d;
    --label-black: #181819;
    --label-black-light: #2a2a2c;
    --accent-orange: #f07a4c;
    --accent-orange-soft: #d9825f;
  }
  html, body {
    margin: 0;
    padding: 0;
    width: 1200px;
    height: 1109px;
    overflow: hidden;
    background: var(--backdrop);
  }
  .canvas {
    display: block;
    width: 1200px;
    height: 1109px;
  }
  .lid-rim { fill: var(--lid-rim); }
  .label-face { fill: url(#labelShade); }
  .label-ring { fill: none; stroke: var(--accent-orange); stroke-width: 3; }
  .rule { stroke: var(--accent-orange); stroke-width: 3; }
  .star { fill: var(--accent-orange); }
  .product-type {
    font-family: "Oswald", sans-serif;
    font-size: 34px;
    letter-spacing: 3px;
    fill: var(--accent-orange);
  }
  .brand-name {
    font-family: "Bebas Neue", sans-serif;
    fill: var(--accent-orange);
  }
  .brand-main { font-size: 250px; letter-spacing: 2px; }
  .brand-sub { font-size: 92px; letter-spacing: 2px; }
  .range-name {
    font-family: "Oswald", sans-serif;
    font-size: 44px;
    letter-spacing: 3px;
    fill: var(--accent-orange);
  }
  .volume {
    font-family: "Oswald", sans-serif;
    font-size: 36px;
    letter-spacing: 4px;
    fill: var(--accent-orange);
  }
  .health-message {
    font-family: "Oswald", sans-serif;
    font-weight: 500;
    font-size: 21px;
    letter-spacing: 2px;
    fill: var(--accent-orange-soft);
  }
</style>
</head>
<body>
<svg class="canvas" viewBox="0 0 1200 1109" xmlns="http://www.w3.org/2000/svg">
  <defs>
    <radialGradient id="labelShade" cx="45%" cy="40%" r="65%">
      <stop offset="0%" stop-color="var(--label-black-light)"/>
      <stop offset="100%" stop-color="var(--label-black)"/>
    </radialGradient>
  </defs>

  <g class="lid">
    <circle class="lid-rim" cx="600" cy="554" r="430"/>
    <circle class="label-face" cx="600" cy="554" r="395"/>
    <circle class="label-ring" cx="600" cy="554" r="372"/>
  </g>

  <g class="rating-stars">
    <polygon class="star" points="510,248 515,260 528,260 518,268 522,281 510,273 498,281 502,268 492,260 505,260"/>
    <polygon class="star" points="555,243 560,255 573,255 563,263 567,276 555,268 543,276 547,263 537,255 550,255"/>
    <polygon class="star" points="600,240 605,252 618,252 608,260 612,273 600,265 588,273 592,260 582,252 595,252"/>
    <polygon class="star" points="645,243 650,255 663,255 653,263 657,276 645,268 633,276 637,263 627,255 640,255"/>
    <polygon class="star" points="690,248 695,260 708,260 698,268 702,281 690,273 678,281 682,268 672,260 685,260"/>
  </g>

  <text class="product-type" x="600" y="330" text-anchor="middle">LIP &amp; TATTOO BALM</text>
  <line class="rule" x1="550" y1="348" x2="650" y2="348"/>

  <text class="brand-name brand-main" x="600" y="590" text-anchor="middle">GRAVEL</text>
  <text class="brand-name brand-sub" x="845" y="672" text-anchor="end">CRAFT</text>

  <g class="divider">
    <line class="rule" x1="395" y1="700" x2="585" y2="700"/>
    <polygon class="star" points="600,690 603,697 611,697 605,702 607,710 600,705 593,710 595,702 589,697 597,697"/>
    <line class="rule" x1="615" y1="700" x2="805" y2="700"/>
  </g>

  <text class="range-name" x="600" y="764" text-anchor="middle">TUSKERS BOTANICAL</text>
  <text class="volume" x="600" y="816" text-anchor="middle">50 ml</text>
  <text class="health-message" x="600" y="862" text-anchor="middle">SPEAK UP · MEN'S HEALTH MATTERS</text>
</svg>
</body>
</html>
```